Brightwell Homes Guide Business card

I have had at the logo designed here and attached. The business compares off the plan apartments in Sydney and provides quick comparison for new home buyers e.g price, floor plans and location. I would like the complimentary colours used on the business card. I would like it be unique but also look professional. I also have a website to gain inspiration from www.brightwellhomesguide.com.au
Updates
Industry/Entity Type
Business
Contact Information for Business Card
Helen Vostrakis
Director of Business Development
e: helen.vostrakis@brightwellhomesguide.com.au
p: (02) 8143 7692
m: 0431 572 908
w: www.brightwellhomesguide.com.au
Look and feel
Each slider illustrates characteristics of the customer's brand and the style your logo design should communicate.

```html
<!DOCTYPE html>
<html lang="en">
<head>
<meta charset="utf-8">
<title>Brightwell Homes Guide – Business Card</title>
<link rel="stylesheet" href="https://fonts.googleapis.com/css2?family=Open+Sans:wght@400;600;700&display=swap">
<style>
  :root {
    --backdrop: #e9e7e4;
    --card: #111111;
    --green: #7dc242;
    --blue: #1c8fd0;
    --ink: #f2f2f2;
    --rule: #6a6a6a;
  }
  * { box-sizing: border-box; margin: 0; padding: 0; }
  html, body { width: 1200px; height: 814px; overflow: hidden; }
  body {
    background: var(--backdrop);
    font-family: "Open Sans", Arial, sans-serif;
    position: relative;
  }
  .card {
    position: absolute;
    top: 248px;
    width: 520px;
    height: 318px;
    background: var(--card);
    border-radius: 3px;
    box-shadow: 0 10px 28px rgba(0,0,0,.25);
  }
  .card--front { left: 50px; }
  .card--back { left: 630px; }

  .brand {
    display: flex;
    align-items: center;
    gap: 10px;
    color: var(--green);
    font-weight: 700;
    line-height: 1;
    white-space: nowrap;
  }
  .brand__mark {
    width: 18px; height: 18px;
    background: var(--blue);
    flex: none;
  }
  .card--front .brand {
    position: absolute;
    left: 64px; top: 70px;
    font-size: 30px;
  }
  .card--back .brand {
    position: absolute;
    left: 0; right: 0; top: 112px;
    justify-content: center;
    font-size: 32px;
  }
  .card--back .brand__mark { width: 20px; height: 20px; }

  .site-url {
    position: absolute;
    left: 0; right: 0; top: 196px;
    text-align: center;
    color: var(--ink);
    font-size: 12px;
    letter-spacing: 2.6px;
  }

  .person {
    position: absolute;
    left: 40px; top: 196px;
    width: 166px;
    text-align: right;
  }
  .person__name { color: var(--green); font-weight: 600; font-size: 19px; line-height: 1.25; }
  .person__title { color: var(--blue); font-size: 12px; line-height: 1.3; margin-top: 3px; }

  .divider {
    position: absolute;
    left: 220px; top: 170px;
    width: 1px; height: 96px;
    background: var(--rule);
  }

  .contacts {
    position: absolute;
    left: 234px; top: 163px;
    list-style: none;
    color: var(--ink);
    font-size: 12px;
    line-height: 21px;
  }
  .contacts li { display: flex; align-items: center; gap: 7px; white-space: nowrap; }
  .contacts svg { width: 11px; height: 11px; flex: none; fill: var(--green); }
  .contacts .social-square {
    width: 10px; height: 10px; background: var(--green); flex: none; margin: 0 1px 0 0;
  }
</style>
</head>
<body>
  <section class="card card--front" aria-label="Business card front">
    <div class="brand"><span class="brand__mark"></span>Brightwell Homes Guide</div>

    <div class="person">
      <p class="person__name">Helen Vostrakis</p>
      <p class="person__title">Director of<br>Business Development</p>
    </div>

    <div class="divider"></div>

    <ul class="contacts">
      <li>
        <svg viewBox="0 0 24 24" aria-hidden="true"><path d="M6.6 10.8a15.1 15.1 0 0 0 6.6 6.6l2.2-2.2c.3-.3.7-.4 1-.2 1.1.4 2.3.6 3.6.6.6 0 1 .4 1 1V20c0 .6-.4 1-1 1A17 17 0 0 1 3 4c0-.6.4-1 1-1h3.5c.6 0 1 .4 1 1 0 1.3.2 2.5.6 3.6.1.3 0 .7-.2 1z"/></svg>
        (02) 8143 7692
      </li>
      <li>
        <svg viewBox="0 0 24 24" aria-hidden="true"><path d="M2 5h20v14H2z M3.5 6.5 12 13l8.5-6.5" fill="none" stroke="#7dc242" stroke-width="2.4"/></svg>
        helen.vostrakis@brightwellhomesguide.com.au
      </li>
      <li>
        <svg viewBox="0 0 24 24" aria-hidden="true"><circle cx="12" cy="12" r="10" fill="none" stroke="#7dc242" stroke-width="2.4"/><path d="M2 12h20M12 2c3 3 3 17 0 20M12 2c-3 3-3 17 0 20" fill="none" stroke="#7dc242" stroke-width="2"/></svg>
        www.brightwellhomesguide.com.au
      </li>
      <li><span class="social-square"></span>brightwellhomesguide</li>
      <li><span class="social-square"></span>brightwellhomesguide</li>
    </ul>
  </section>

  <section class="card card--back" aria-label="Business card back">
    <div class="brand"><span class="brand__mark"></span>Brightwell Homes Guide</div>
    <p class="site-url">www.brightwellhomesguide.com.au</p>
  </section>
</body>
</html>
```